Etiketten für Olivenöl-Intensivcreme
Zielgruppe
Wir produzieren Bio-Food, u.a. Wein und Olivenöl. Jetzt soll eine Olivenöl-Intensivcreme im Bereich Kosmetik auf dem Markt platziert werden. Unsere Zielgruppe hat ein sehr breites Altersspektrum (jung bis alt), ist naturverbunden, tierlieb, gebildet, kritisch-reflektierend, weiß gute Qualität zu schätzen, ist überwiegend weiblich. Die Olivenöl-Intensivcreme hat eine sehr breite Verwendung und soll sich als 'Allzweckwaffe' in jedem Haushalt etablieren (Babyhaut-Pflege, Lippenpflege, Ganzkörperpflege, Hand-Schutzcreme etc.).
Aufgabenstellung
Die Creme soll heißen: Tavunel (es könnte z.B. der Buchstabe 'O' durch eine Olive ersetzt werden). Es gibt zwei Etikette (Deckeloberseite der Metalldose und auf dem Boden). Der Durchmesser der Etikette ist jeweils 5,5 cm. Die Deckelunterseite gilt reinen Pflichtangaben. Im Dateidownloadbereich sind die Textvorgaben für die Etikette. MUT zur Farbe! Wir sind NICHT brav und angepasst! Orange kann Akzente setzen bzw. für Aufmerksamkeit im Regal sorgen.

```html
<!DOCTYPE html>
<html lang="de">
<head>
<meta charset="utf-8">
<title>Tavunel – Deckeletikett</title>
<link rel="stylesheet" href="https://fonts.googleapis.com/css2?family=Barlow+Semi+Condensed:wght@400;500&family=Roboto+Slab:wght@400&display=swap">
<style>
  :root {
    --label-orange: #ef8152;
    --rim-grey: #c9c9c9;
    --ink-black: #1d1d1b;
    --paper-white: #ffffff;
    --soft-white: rgba(255, 255, 255, 0.85);
    --mark-tint: rgba(255, 255, 255, 0.35);
    --canvas-bg: #ffffff;
  }
  html, body {
    margin: 0;
    padding: 0;
    width: 1200px;
    height: 1160px;
    overflow: hidden;
    background: var(--canvas-bg);
  }
  .canvas {
    position: relative;
    width: 1200px;
    height: 1160px;
  }
  .lid-label {
    position: absolute;
    left: 90px;
    top: 70px;
    width: 1020px;
    height: 1020px;
    border-radius: 50%;
    background: var(--label-orange);
    box-shadow: 0 0 0 18px var(--rim-grey);
    overflow: hidden;
    font-family: "Barlow Semi Condensed", "Arial Narrow", sans-serif;
  }
  .brand-mark {
    position: absolute;
    left: 462px;
    top: 70px;
    width: 96px;
    height: 96px;
    border-radius: 50%;
    background: var(--mark-tint);
  }
  .brand-name {
    position: absolute;
    top: 196px;
    left: 0;
    width: 100%;
    text-align: center;
    color: var(--paper-white);
    font-size: 62px;
    font-weight: 400;
    line-height: 1;
    letter-spacing: 0.5px;
  }
  .natural-badge {
    position: absolute;
    left: 683px;
    top: 218px;
    width: 232px;
    height: 232px;
    border-radius: 50%;
    background: var(--ink-black);
    color: var(--paper-white);
    display: flex;
    align-items: center;
    justify-content: center;
    text-align: center;
    font-size: 44px;
    font-weight: 500;
    line-height: 1.12;
  }
  .olive-branch {
    position: absolute;
    left: 44px;
    top: 330px;
    width: 286px;
    height: 150px;
    border-radius: 50% 50% 50% 50% / 60% 60% 40% 40%;
    background: linear-gradient(160deg, var(--paper-white), var(--soft-white));
  }
  .product-name {
    position: absolute;
    margin: 0;
    top: 442px;
    left: 190px;
    color: var(--paper-white);
    font-family: "Roboto Slab", Georgia, serif;
    font-size: 200px;
    font-weight: 400;
    line-height: 1;
    letter-spacing: -2px;
    white-space: nowrap;
  }
  .product-type {
    position: absolute;
    top: 656px;
    left: 0;
    width: 100%;
    text-align: center;
    color: var(--ink-black);
    font-size: 66px;
    font-weight: 500;
    letter-spacing: 0.3px;
  }
  .product-claims {
    position: absolute;
    margin: 0;
    top: 778px;
    left: 0;
    width: 100%;
    text-align: center;
    color: var(--paper-white);
    font-size: 54px;
    font-weight: 400;
    line-height: 1.3;
  }
</style>
</head>
<body>
  <main class="canvas">
    <section class="lid-label">
      <div class="brand-mark" aria-hidden="true"></div>
      <div class="brand-name">KELVARO.LAND</div>
      <div class="natural-badge">NATUR-<br>KOSMETIK</div>
      <div class="olive-branch" role="img" aria-label="Olivenzweig mit zwei weißen Blättern"></div>
      <h1 class="product-name">Tavunel</h1>
      <div class="product-type">OLIVENÖL-INTENSIVCREME</div>
      <p class="product-claims">Bio-Olive . vegan . Pflege-<br>und Schutzcreme</p>
    </section>
  </main>
</body>
</html>
```